Velmora Works Brochure Design Project

Our company requires a brochure for promoting our Corporate Training business.

Please use data from Corporate training brochure doc.

Dear Designers,

We have added new corporate brochure document into the project. Use this data to finish up your brochure.

Thanks,

Omar deswick

Reason: We have recently finalised the data that will go into the corporate brochure.

Reason: To get more better designs

Target Market(s)

Training Managers / Business Managers / Hiring Managers

Industry/Entity Type

Training

Requirements
Must have
• Corporate and Professional Look

```html
<!DOCTYPE html>
<html lang="en">
<head>
<meta charset="utf-8">
<title>Velmora Works — Corporate Training Brochure Cover</title>
<link rel="stylesheet" href="https://fonts.googleapis.com/css2?family=Cinzel:wght@400;500&display=swap">
<style>
  :root {
    --cover-teal: #4d676c;
    --cover-teal-deep: #2f4447;
    --header-slate: #354b4e;
    --tile-light: #e4ecee;
    --tile-mid: #9fb3b7;
    --tile-dark: #6b8489;
    --gold-bright: #f7cc2a;
    --gold-deep: #e2a50c;
    --title-gold: #ecd027;
    --headline-white: #f2f4f4;
    --photo-warm: #c9a88c;
    --photo-cool: #7f9390;
  }
  * { margin: 0; padding: 0; box-sizing: border-box; }
  html, body { width: 849px; height: 1200px; overflow: hidden; background: var(--cover-teal); }
  .cover {
    position: relative;
    width: 849px;
    height: 1200px;
    overflow: hidden;
    background: radial-gradient(ellipse at 30% 40%, #557176 0%, var(--cover-teal) 60%, #465f63 100%);
    font-family: "Cinzel", "Trajan Pro", serif;
  }
  .cover-art { position: absolute; inset: 0; width: 849px; height: 1200px; }
  .masthead {
    position: absolute;
    left: 67px; top: 160px;
    width: 508px; height: 155px;
    background: var(--header-slate);
    display: flex; align-items: center; justify-content: center;
    padding-top: 18px;
  }
  .company-name {
    color: var(--title-gold);
    font-size: 27px;
    font-weight: 400;
    line-height: 34px;
    text-align: center;
    letter-spacing: 0.5px;
  }
  .team-photo {
    position: absolute;
    left: 67px; top: 315px;
    width: 508px; height: 340px;
    background:
      radial-gradient(ellipse at 85% 25%, #a9c29c 0%, transparent 45%),
      radial-gradient(ellipse at 30% 70%, var(--photo-warm) 0%, transparent 55%),
      linear-gradient(90deg, #2e3538 0%, #55605f 40%, var(--photo-cool) 70%, #c7d3c8 100%);
  }
  .accent-band {
    position: absolute;
    top: 359px; height: 41px;
    background: linear-gradient(180deg, var(--gold-bright) 0%, #f3bd1c 55%, var(--gold-deep) 100%);
    box-shadow: 0 2px 4px rgba(0,0,0,0.25);
  }
  .accent-band--left { left: 0; width: 98px; }
  .accent-band--right { left: 538px; width: 311px; }
  .headline {
    position: absolute;
    left: 67px; top: 697px;
    width: 516px;
    color: var(--headline-white);
    font-size: 29px;
    font-weight: 400;
    line-height: 34px;
    text-align: center;
    letter-spacing: 0.5px;
  }
</style>
</head>
<body>
  <main class="cover">
    <svg class="cover-art" viewBox="0 0 849 1200" xmlns="http://www.w3.org/2000/svg">
      <defs>
        <linearGradient id="tileSweep" x1="0" y1="0" x2="1" y2="0.3">
          <stop offset="0" stop-color="var(--tile-dark)"/>
          <stop offset="0.35" stop-color="var(--tile-mid)"/>
          <stop offset="0.75" stop-color="var(--tile-light)"/>
          <stop offset="1" stop-color="#cfdadc"/>
        </linearGradient>
        <linearGradient id="cornerShade" x1="0" y1="0" x2="1" y2="1">
          <stop offset="0" stop-color="#2a3c3f"/>
          <stop offset="1" stop-color="var(--cover-teal-deep)"/>
        </linearGradient>
        <filter id="curlShadow" x="-20%" y="-5%" width="140%" height="110%">
          <feGaussianBlur stdDeviation="9"/>
        </filter>
      </defs>
      <path d="M531 0 C 640 90, 650 250, 630 470 C 612 690, 560 880, 470 1200 L 849 1200 L 849 0 Z"
            fill="#1f2f31" opacity="0.55" filter="url(#curlShadow)"/>
      <path class="tile-sweep" role="img" aria-label="Decorative sweep of soft grey-teal mosaic tiles curling down the right edge"
            d="M541 0 C 650 90, 660 250, 640 470 C 622 690, 570 880, 484 1200 L 849 1200 L 849 0 Z"
            fill="url(#tileSweep)"/>
      <path class="corner-fold" d="M442 1200 C 500 1080, 560 1010, 650 970 C 730 935, 800 915, 849 910 L 849 1200 Z"
            fill="url(#cornerShade)"/>
    </svg>

    <header class="masthead">
      <h1 class="company-name">Velmora<br>Works</h1>
    </header>

    <div class="team-photo" role="img" aria-label="Photo of four smiling business colleagues standing in a row along a bright office corridor"></div>

    <div class="accent-band accent-band--left"></div>
    <div class="accent-band accent-band--right"></div>

    <h2 class="headline">Corporate training<br>in 2012</h2>
  </main>
</body>
</html>
```